Alaska Law Firm Needs a Sticker Design

We need a design for stickers to put on already-printed brochures. We mail the brochures to potential clients so they can learn more about accident-induced injuries, insurance claims, legal representation, and our own law firm.

One of our lawyers wrote a book that provides a helpful overview of personal injury claims. We are offering this book for free to anyone who calls and requests it. Therefore, the sticker design should include one of the following phrases, or something very similar:
a) "Still have questions? Call and request our book-- for free!"
b) "Still have questions about auto accident claims? Call and request our book today."
c) "Still have questions about filing a claim? Call and request a free copy of our book."
d) "Still have questions? Call us today to request a free copy of our book, Clear Lanes Ahead."
e) "To learn more about automobile accidents and insurance, call today and request a free copy of our book."

The sticker should be approximately 3"x3" and may be a circle, square, rectangle, or ellipsis. The sticker will be placed on the back of the folder, which is light blue. We would like the sticker to match the color scheme of our website and the folder.

I will upload an image of the book cover as soon as I obtain it.

Industry/Entity Type

Law Firm

Font styles to use
Serif
Sans Serif

Requirements
Should not have
• Bright colors that aren't already used in the folder design. e.g. no bright orange, pink, chartreuse, turquoise, yellow, red.

```html
<!DOCTYPE html>
<html lang="en">
<head>
<meta charset="UTF-8">
<title>Free Book Sticker</title>
<link rel="stylesheet" href="https://fonts.googleapis.com/css2?family=Open+Sans:wght@400;600&display=swap">
<style>
  :root {
    --bg: #e9e9e9;
    --navy: #0e3a66;
    --ink-gray: #6a6a6a;
    --ring-gray: #5c5c5c;
    --sticker-blue: #97c2ea;
    --white: #ffffff;
  }
  html, body {
    margin: 0;
    padding: 0;
    width: 1200px;
    height: 1200px;
    overflow: hidden;
    background: radial-gradient(circle at 50% 45%, #f4f4f4 0%, var(--bg) 70%);
  }
  .canvas {
    width: 1200px;
    height: 1200px;
    display: flex;
    align-items: center;
    justify-content: center;
  }
  .sticker {
    width: 1000px;
    height: 966px;
    display: block;
  }
  .sticker-text {
    font-family: "Open Sans", sans-serif;
    font-weight: 400;
  }
  .t-navy { fill: var(--navy); }
  .t-gray { fill: var(--ink-gray); }
  .t-white { fill: var(--white); }
  .caller-area { fill: var(--navy); }
</style>
</head>
<body>
<main class="canvas">
  <svg class="sticker" viewBox="320 40 580 560" xmlns="http://www.w3.org/2000/svg" aria-label="Sticker: To learn more about automobile accidents and insurance, call today and request a free copy of our book.">
    <circle class="ring-gray" cx="605" cy="296" r="255" fill="var(--ring-gray)"/>
    <circle class="ring-navy" cx="626" cy="322" r="255" fill="var(--navy)"/>
    <circle class="ring-white" cx="590" cy="332" r="260" fill="var(--white)"/>
    <circle class="sticker-face" cx="602" cy="316" r="246" fill="var(--sticker-blue)"/>

    <g class="sticker-text">
      <text x="462" y="190"><tspan class="t-navy" font-size="36">"To learn </tspan><tspan class="t-navy" font-size="48">more</tspan></text>
      <text x="437" y="236"><tspan class="t-navy" font-size="48">about </tspan><tspan class="t-gray" font-size="31">automobile</tspan></text>
      <text x="439" y="288"><tspan class="t-white" font-size="54">accidents </tspan><tspan class="t-navy" font-size="34">and</tspan></text>
      <text x="500" y="340"><tspan class="t-navy" font-size="58">insurance,</tspan></text>
      <text x="494" y="380"><tspan class="t-navy" font-size="35">today </tspan><tspan class="t-gray" font-size="33">and request</tspan></text>
      <text x="510" y="424"><tspan class="t-gray" font-size="39">a free copy</tspan></text>
      <text x="454" y="480"><tspan class="t-navy" font-size="52">of our book."</tspan></text>
    </g>

    <g class="caller">
      <rect class="caller-area" x="402" y="298" width="86" height="106" rx="10" role="img" aria-label="Caller on the phone icon"/>
      <text x="432" y="397" class="sticker-text t-white" font-size="30">call</text>
    </g>
  </svg>
</main>
</body>
</html>
```